Piano teaching business needs a business card and logo design.

We provide piano lessons to children and adults. The card / logo should be colourful and playful and appeal to kids but retain a professional mature approach which also appeals to adults. I like the Colours orange and blue as dominating theme colours, but we are open to all colour ideas. The business name is: BLUE OWL SWING. We do not like typical black and white images of piano keyboards. A cartoon character of a jazz inspired orange coloured fat cat playing piano is one idea but we are open to all ideas.

Target Market(s)

Domestic, Local population, adults and children.

Industry/Entity Type

Service

Contact Information for Business Card

Piano teacher
Mel T Karsh
27 Wendover Close
Arundel
4214 QLD
T: 07 5283 9147
M: 0438 752 906
E: keyvale@mailbrook.net
www. keyvale.net.au

Logo Text

Blue Owl Swing

Font styles to use
Sans Serif

Colors
f78f20
f37122
0493ce
0455a3
fbed22

Requirements
Must have
• Colours.
Nice to have
• Cartoon style fat cat. Limited music notation.
Should not have
• Dominating images of keyboards.

```html
<!DOCTYPE html>
<html lang="en">
<head>
<meta charset="utf-8">
<title>Blue Owl Swing – Business Card</title>
<link rel="stylesheet" href="https://fonts.googleapis.com/css2?family=Fira+Sans:wght@600&family=Raleway:wght@400;500;600;700&display=swap">
<style>
  :root {
    --page-bg: #efefef;
    --sky-light: #aae9fc;
    --sky-mid: #97e3fc;
    --sky-deep: #84dffd;
    --halo: #ffffff;
    --brand-blue: #1a5ea8;
    --ink: #111111;
    --art-orange: #f37122;
    --art-orange-soft: #f79a5a;
  }
  * { margin: 0; padding: 0; box-sizing: border-box; }
  html, body {
    width: 1200px;
    height: 609px;
    overflow: hidden;
    background: var(--page-bg);
  }
  .card {
    position: absolute;
    left: 357px;
    top: 139px;
    width: 484px;
    height: 302px;
    overflow: hidden;
    background: var(--sky-light);
    box-shadow: 0 1px 4px rgba(0,0,0,0.12);
  }
  .card-backdrop {
    position: absolute;
    inset: 0;
  }
  .mascot-art {
    position: absolute;
    left: 18px;
    top: 34px;
    width: 220px;
    height: 243px;
    border-radius: 50%;
    background: linear-gradient(160deg, var(--art-orange-soft), var(--art-orange));
  }
  .line {
    position: absolute;
    right: 28px;
    line-height: 1;
    white-space: nowrap;
    text-align: right;
  }
  .business-name {
    top: 29px;
    font-family: "Fira Sans", sans-serif;
    font-weight: 600;
    font-size: 33px;
    color: var(--brand-blue);
  }
  .person-name {
    top: 74px;
    font-family: "Raleway", sans-serif;
    font-weight: 600;
    font-size: 24px;
    color: var(--brand-blue);
  }
  .role {
    top: 98px;
    font-family: "Raleway", sans-serif;
    font-weight: 500;
    font-size: 19px;
    color: var(--ink);
  }
  .address {
    font-family: "Raleway", sans-serif;
    font-weight: 400;
    font-size: 17.5px;
    color: var(--ink);
  }
  .address-street { top: 140px; }
  .address-town { top: 156px; }
  .phone {
    font-family: "Raleway", sans-serif;
    font-weight: 700;
    font-size: 21px;
    color: var(--brand-blue);
  }
  .phone .label {
    font-weight: 400;
    font-size: 17px;
    margin-right: 3px;
  }
  .phone-landline { top: 191px; }
  .phone-mobile { top: 212px; }
  .email {
    top: 246px;
    font-family: "Raleway", sans-serif;
    font-weight: 400;
    font-size: 16.5px;
    color: var(--brand-blue);
  }
  .website {
    top: 262px;
    font-family: "Raleway", sans-serif;
    font-weight: 600;
    font-size: 16.5px;
    color: var(--brand-blue);
  }
</style>
</head>
<body>
  <section class="card">
    <svg class="card-backdrop" width="484" height="302" viewBox="0 0 484 302" aria-hidden="true">
      <defs>
        <linearGradient id="right-wash" x1="0" y1="0" x2="1" y2="0">
          <stop offset="0" stop-color="#ffffff" stop-opacity="0.7"/>
          <stop offset="0.35" stop-color="#97e3fc"/>
          <stop offset="1" stop-color="#84dffd"/>
        </linearGradient>
      </defs>
      <rect width="484" height="302" fill="#aae9fc"/>
      <path d="M220 0 H484 V302 H220 A330 330 0 0 0 220 0 Z" fill="url(#right-wash)"/>
      <circle cx="110" cy="155" r="200" fill="#aae9fc"/>
      <path d="M0 30 Q60 2 140 0" stroke="#ffffff" stroke-opacity="0.6" stroke-width="6" fill="none"/>
      <circle cx="114" cy="178" r="115" fill="#ffffff"/>
    </svg>
    <div class="mascot-art" role="img" aria-label="Cartoon mascot illustration: a jolly cat in an orange jacket playing a blue keyboard"></div>

    <h1 class="line business-name">BLUE OWL SWING</h1>
    <p class="line person-name">Mel T Karsh</p>
    <p class="line role">Piano teacher</p>
    <p class="line address address-street">27 Wendover Close</p>
    <p class="line address address-town">Arundel 4214 QLD</p>
    <p class="line phone phone-landline"><span class="label">t:</span>07 5283 9147</p>
    <p class="line phone phone-mobile"><span class="label">m:</span>0438 752 906</p>
    <p class="line email">E: keyvale@mailbrook.net</p>
    <p class="line website">www. keyvale.net.au</p>
  </section>
</body>
</html>
```